Custom Mexican Train Dominos Scorecard

My wife and I regularly play Mexican Train dominos with our friends and family and would like to create a series of custom scorecards specific to our various groups that we play with. The idea would be to have them printed on pads or in notebooks that over time will hold a record of all of our games. Searching around on the web, the only "off the shelf" that I see are pretty plain and boring (see attached). We would love something with a fun and playful mid-century graphic feel to it. Can be a single color or more than one. We want to have the player names incorporated into the design, so for the first one the names would be Carla, Douglas, Ruth & Oliver. We will want a place to date each card and of course boxes to fill out the score. I have included a few examples of how the scorecard is basically laid out. Can be any size and can be done in landscape or portrait. I think I would just like the title to say "Domino Night" or potentially no title at all with just a fun domino graphic. Thank you!

Requirements
Must have
• Basic score layout
Nice to have
• nothing in particular
Should not have
• nothing in particular

```html
<!DOCTYPE html>
<html lang="en">
<head>
<meta charset="utf-8">
<title>Domino Night Scorecard</title>
<link href="https://fonts.googleapis.com/css2?family=Alegreya+Sans:wght@400;500&family=Playfair+Display:wght@500&display=swap" rel="stylesheet">
<style>
  :root {
    --red: #e8202a;
    --orange-red: #ef5430;
    --green: #a9d152;
    --line: #c9c9cb;
    --shade: #f3f3f4;
    --paper: #ffffff;
    --train-red: #d8262c;
    --train-blue: #2d6fb6;
    --train-yellow: #f4c21b;
  }
  html, body { margin: 0; padding: 0; overflow: hidden; }
  body { width: 853px; height: 1200px; background: var(--paper); position: relative; font-family: "Alegreya Sans", sans-serif; }
  .masthead { position: absolute; left: 0; top: 0; width: 853px; height: 128px; border: 1px solid #e2e2e4; box-sizing: border-box; background: linear-gradient(#f7f7f8, #ffffff); }
  .corner-pattern { position: absolute; }
  .corner-pattern.left { left: 0; top: 55px; width: 105px; height: 72px; background: linear-gradient(135deg, #f7b49b, #9fd3d9 60%, #f6e27a); clip-path: polygon(0 0, 100% 100%, 0 100%); opacity: .6; }
  .corner-pattern.right { right: 0; top: 0; width: 105px; height: 75px; background: linear-gradient(135deg, #9fd3d9, #f7b49b 60%, #f6e27a); clip-path: polygon(0 0, 100% 0, 100% 100%); opacity: .6; }
  .title-train { position: absolute; left: 158px; top: 4px; width: 537px; height: 110px; border-radius: 10px;
    background: linear-gradient(90deg, var(--train-red) 0 36%, var(--train-blue) 36% 40%, var(--train-yellow) 40% 64%, var(--train-red) 64% 100%); opacity: .85; }

  .score-grid { position: absolute; left: 0; top: 134px; width: 853px; display: grid;
    grid-template-columns: 241px 157px 152px 152px 151px;
    grid-template-rows: 76px repeat(14, 64px);
    border-top: 1px solid var(--line); }
  .score-grid > div { border-bottom: 1px solid var(--line); border-left: 1px solid var(--line); box-sizing: border-box; display: flex; align-items: center; overflow: hidden; }
  .score-grid > div:nth-child(5n+1) { border-left: none; }
  .score-grid .shaded { background: var(--shade); }
  .player-label, .player-name { color: var(--red); font-size: 29px; justify-content: center; line-height: 1; }
  .player-label { justify-content: flex-start; padding-left: 38px; }
  .pip-label { padding-left: 24px; gap: 5px; }
  .pip-label svg { width: 49px; height: 49px; flex: none; }
  .pip-value { font-family: "Playfair Display", serif; font-variant-numeric: lining-nums; color: var(--green); font-size: 47px; width: 72px; text-align: center; margin-left: 20px; line-height: 1; }
  .subtotal-label { color: var(--orange-red); font-size: 28px; padding-left: 25px; line-height: 1; }

  .game-total { position: absolute; left: 0; top: 1113px; width: 853px; height: 53px; display: grid;
    grid-template-columns: 244px 152px 152px 152px 153px; border-top: 1px solid var(--line); border-bottom: 1px solid var(--line); }
  .game-total > div { border-left: 1px solid var(--line); display: flex; align-items: center; }
  .game-total > div:first-child { border-left: none; color: var(--red); font-size: 28px; padding-left: 36px; line-height: 1; }
  .footer-rule { position: absolute; left: 0; top: 1169px; width: 853px; border-top: 1px solid var(--line); }
  .date-field { position: absolute; right: 152px; top: 1173px; color: var(--red); font-size: 28px; line-height: 1; }
</style>
</head>
<body>
<svg width="0" height="0" style="position:absolute" aria-hidden="true">
  <defs>
    <symbol id="h0" viewBox="0 0 60 60"><rect width="60" height="60" rx="9" fill="#a9d152"/></symbol>
    <symbol id="h1" viewBox="0 0 60 60"><use href="#h0"/><g fill="#fff"><circle cx="30" cy="30" r="5"/></g></symbol>
    <symbol id="h2" viewBox="0 0 60 60"><use href="#h0"/><g fill="#fff"><circle cx="12" cy="12" r="5"/><circle cx="48" cy="48" r="5"/></g></symbol>
    <symbol id="h3" viewBox="0 0 60 60"><use href="#h2"/><circle cx="30" cy="30" r="5" fill="#fff"/></symbol>
    <symbol id="h4" viewBox="0 0 60 60"><use href="#h2"/><g fill="#fff"><circle cx="48" cy="12" r="5"/><circle cx="12" cy="48" r="5"/></g></symbol>
    <symbol id="h5" viewBox="0 0 60 60"><use href="#h4"/><circle cx="30" cy="30" r="5" fill="#fff"/></symbol>
    <symbol id="h6" viewBox="0 0 60 60"><use href="#h0"/><g fill="#fff"><circle cx="12" cy="15" r="5"/><circle cx="30" cy="15" r="5"/><circle cx="48" cy="15" r="5"/><circle cx="12" cy="45" r="5"/><circle cx="30" cy="45" r="5"/><circle cx="48" cy="45" r="5"/></g></symbol>
    <symbol id="h7" viewBox="0 0 60 60"><use href="#h0"/><g fill="#fff"><circle cx="12" cy="12" r="5"/><circle cx="30" cy="12" r="5"/><circle cx="48" cy="12" r="5"/><circle cx="30" cy="30" r="5"/><circle cx="12" cy="48" r="5"/><circle cx="30" cy="48" r="5"/><circle cx="48" cy="48" r="5"/></g></symbol>
    <symbol id="h8" viewBox="0 0 60 60"><use href="#h0"/><g fill="#fff"><circle cx="12" cy="12" r="5"/><circle cx="30" cy="12" r="5"/><circle cx="48" cy="12" r="5"/><circle cx="12" cy="30" r="5"/><circle cx="48" cy="30" r="5"/><circle cx="12" cy="48" r="5"/><circle cx="30" cy="48" r="5"/><circle cx="48" cy="48" r="5"/></g></symbol>
    <symbol id="h9" viewBox="0 0 60 60"><use href="#h8"/><circle cx="30" cy="30" r="5" fill="#fff"/></symbol>
    <symbol id="h10" viewBox="0 0 60 60"><use href="#h0"/><g fill="#fff"><circle cx="9" cy="12" r="4.5"/><circle cx="23" cy="12" r="4.5"/><circle cx="37" cy="12" r="4.5"/><circle cx="51" cy="12" r="4.5"/><circle cx="9" cy="30" r="4.5"/><circle cx="51" cy="30" r="4.5"/><circle cx="9" cy="48" r="4.5"/><circle cx="23" cy="48" r="4.5"/><circle cx="37" cy="48" r="4.5"/><circle cx="51" cy="48" r="4.5"/></g></symbol>
    <symbol id="h11" viewBox="0 0 60 60"><use href="#h10"/><circle cx="30" cy="30" r="4.5" fill="#fff"/></symbol>
    <symbol id="h12" viewBox="0 0 60 60"><use href="#h10"/><g fill="#fff"><circle cx="23" cy="30" r="4.5"/><circle cx="37" cy="30" r="4.5"/></g></symbol>
  </defs>
</svg>

<header class="masthead">
  <div class="corner-pattern left" role="img" aria-label="Scattered colourful domino tiles pattern"></div>
  <div class="corner-pattern right" role="img" aria-label="Scattered colourful domino tiles pattern"></div>
  <div class="title-train" role="img" aria-label="Toy train illustration pulling three wagons carrying block letters spelling Domino Night"></div>
</header>

<main class="score-grid">
  <div class="shaded player-label">Player Names</div>
  <div class="shaded player-name">Carla</div>
  <div class="shaded player-name">Douglas</div>
  <div class="shaded player-name">Ruth</div>
  <div class="shaded player-name">Oliver</div>

  <div class="shaded pip-label"><svg><use href="#h12"/></svg><svg><use href="#h12"/></svg><span class="pip-value">12</span></div><div class="shaded"></div><div class="shaded"></div><div class="shaded"></div><div class="shaded"></div>
  <div class="shaded pip-label"><svg><use href="#h11"/></svg><svg><use href="#h11"/></svg><span class="pip-value">11</span></div><div class="shaded"></div><div class="shaded"></div><div class="shaded"></div><div class="shaded"></div>
  <div class="shaded pip-label"><svg><use href="#h10"/></svg><svg><use href="#h10"/></svg><span class="pip-value">10</span></div><div class="shaded"></div><div class="shaded"></div><div class="shaded"></div><div class="shaded"></div>
  <div class="shaded pip-label"><svg><use href="#h9"/></svg><svg><use href="#h9"/></svg><span class="pip-value">9</span></div><div class="shaded"></div><div class="shaded"></div><div class="shaded"></div><div class="shaded"></div>
  <div class="shaded pip-label"><svg><use href="#h8"/></svg><svg><use href="#h8"/></svg><span class="pip-value">8</span></div><div class="shaded"></div><div class="shaded"></div><div class="shaded"></div><div class="shaded"></div>
  <div class="shaded pip-label"><svg><use href="#h7"/></svg><svg><use href="#h7"/></svg><span class="pip-value">7</span></div><div class="shaded"></div><div class="shaded"></div><div class="shaded"></div><div class="shaded"></div>
  <div class="shaded pip-label"><svg><use href="#h6"/></svg><svg><use href="#h6"/></svg><span class="pip-value">6</span></div><div class="shaded"></div><div class="shaded"></div><div class="shaded"></div><div class="shaded"></div>
  <div class="shaded subtotal-label">Sub Total</div><div class="shaded"></div><div class="shaded"></div><div class="shaded"></div><div class="shaded"></div>

  <div class="pip-label"><svg><use href="#h5"/></svg><svg><use href="#h5"/></svg><span class="pip-value">5</span></div><div></div><div></div><div></div><div></div>
  <div class="pip-label"><svg><use href="#h4"/></svg><svg><use href="#h4"/></svg><span class="pip-value">4</span></div><div></div><div></div><div></div><div></div>
  <div class="pip-label"><svg><use href="#h3"/></svg><svg><use href="#h3"/></svg><span class="pip-value">3</span></div><div></div><div></div><div></div><div></div>
  <div class="pip-label"><svg><use href="#h2"/></svg><svg><use href="#h2"/></svg><span class="pip-value">2</span></div><div></div><div></div><div></div><div></div>
  <div class="pip-label"><svg><use href="#h1"/></svg><svg><use href="#h1"/></svg><span class="pip-value">1</span></div><div></div><div></div><div></div><div></div>
  <div class="pip-label"><svg><use href="#h0"/></svg><svg><use href="#h0"/></svg><span class="pip-value">0</span></div><div></div><div></div><div></div><div></div>
</main>

<section class="game-total">
  <div>Game Total</div><div></div><div></div><div></div><div></div>
</section>
<div class="footer-rule"></div>
<div class="date-field">Date :</div>
</body>
</html>
```